Smogline Atlas

Build a simple scrollable "floating" website - Website should have polished, modern look.
Domain has been bought on NameKettle and website should be setup there.
Project Brief:
https://slides.brindlepost.net/deck/7QxKp2vR9tLm4Wz8Ha3NcYe5Bj6Uf1Gd0SoVi/view?mode=shared
Input Files:
https://www.parcelvault.io/f/k3mr81zq5ex7wd2/BXKTpnLdYv9Qe_hRjG4wFs6ox?dl=0

```html
<!DOCTYPE html>
<html lang="en">
<head>
<meta charset="utf-8">
<title>Smogline Atlas Hong Kong</title>
<link rel="stylesheet" href="https://fonts.googleapis.com/css2?family=Open+Sans:wght@300;400;600&display=swap">
<style>
:root{
  --teal:#1d7b82;
  --teal-soft:#2a8d93;
  --ink:#222;
  --white:#fff;
  --mist:#e3e7ea;
  --band:#e6e9eb;
  --footer:#262626;
  --footer-deep:#1e1e1e;
  --gold:#c9a54c;
  --muted:#9a9a9a;
}
*{box-sizing:border-box;margin:0;padding:0}
html,body{width:1200px;height:3495px;overflow:hidden}
body{font-family:"Open Sans",Arial,sans-serif;color:var(--ink);background:var(--white);position:relative}
.abs{position:absolute}
/* hero */
.hero{left:0;top:0;width:1200px;height:838px;background:linear-gradient(180deg,#6f7377 0%,#55595c 40%,#4a4d50 75%,#5d6063 100%)}
.hero-nav{left:0;top:0;width:1200px;height:155px;border-bottom:1px solid rgba(255,255,255,.35)}
.brand{left:66px;top:36px;display:flex;align-items:center;gap:14px;color:var(--white);font-size:26px;font-weight:600}
.brand-dot{width:54px;height:54px;border-radius:50%;background:var(--teal)}
.menu{right:34px;top:58px;display:flex;gap:31px;font-size:26px;color:var(--white);font-weight:400}
.hero-title{left:0;width:1200px;top:310px;text-align:center;color:var(--white);font-size:64px;font-weight:600;letter-spacing:.3px}
.hero-sub{left:0;width:1200px;top:418px;text-align:center;color:var(--white);font-size:31px;line-height:38px}
.circle-arrow{width:62px;height:62px}
/* welcome */
.welcome-title{left:0;width:1200px;top:866px;text-align:center;color:var(--teal);font-size:44px;font-weight:400}
.welcome-text{left:326px;width:600px;top:946px;font-size:22px;line-height:31px}
/* water */
.water{left:0;top:1048px;width:1200px;height:434px;background:linear-gradient(180deg,#5f6a70 0%,#7d8a8f 45%,#9aa3a2 75%,#6d7576 100%)}
.water-title{left:0;width:1200px;top:1115px;text-align:center;color:var(--white);font-size:72px;font-weight:300}
.water-text{left:128px;width:970px;top:1233px;color:var(--white);font-size:26px;line-height:34px}
.btn-outline{left:501px;top:1382px;width:175px;height:51px;border:2px solid var(--white);border-radius:26px;color:var(--white);font-size:20px;text-align:center;line-height:47px}
/* expedition */
.exp-heading{left:64px;top:1706px;font-size:54px;line-height:66px;font-weight:400}
.exp-text{left:373px;top:1522px;width:292px;font-size:22px;line-height:26.4px}
.exp-photo{left:692px;top:1482px;width:508px;height:587px;background:linear-gradient(160deg,#8e9a8a 0%,#6f7a74 40%,#9aa1a2 60%,#5d5a52 100%)}
/* partners */
.partners{left:0;top:2069px;width:1200px;height:214px;background:var(--band)}
/* works */
.section-title{left:0;width:1200px;text-align:center;font-size:44px;font-weight:400}
.card{top:2388px;width:308px;height:385px;background:var(--white);box-shadow:0 4px 6px rgba(0,0,0,.25)}
.card-img{width:308px;height:280px}
.card-tag{margin-top:12px;text-align:center;color:var(--teal);font-size:22px;line-height:26px;font-weight:600}
.card-text{margin:4px 0 0 48px;font-size:21px;line-height:27px;width:240px}
/* note */
.note{left:0;top:2819px;width:1200px;height:364px;background:var(--mist)}
.field{background:var(--white);border-radius:14px;font-size:22px;padding:10px 24px}
.submit{left:534px;top:3111px;width:139px;height:46px;background:var(--teal);color:var(--white);border-radius:14px;font-size:21px;text-align:center;line-height:46px}
/* footer */
.footer{left:0;top:3183px;width:1200px;height:256px;background:var(--footer)}
.foot-col{top:3222px;display:flex;flex-direction:column;gap:21px;font-size:21px;line-height:25px}
.foot-col.gold{color:var(--gold)}
.foot-col.light{color:#cfcfcf}
.foot-about-title{left:800px;top:3222px;color:var(--teal-soft);font-size:27px}
.foot-about{left:800px;top:3292px;width:340px;color:var(--muted);font-size:18px;line-height:23px}
.legal{left:0;top:3439px;width:1200px;height:56px;background:var(--footer-deep);border-top:1px solid #555;color:var(--white);font-size:21px;text-align:center;line-height:54px}
</style>
</head>
<body>

<div class="abs hero" role="img" aria-label="Photo of a busy Hong Kong street with trucks and traffic"></div>
<div class="abs hero-nav"></div>
<div class="abs brand"><span class="brand-dot"></span>Shoreloop</div>
<nav class="abs menu"><span>Trash Sites</span><span>Raw Data</span><span>Expedition</span><span>Supporters</span><span>Get in Touch</span></nav>
<h1 class="abs hero-title">Smogline Atlas Hong Kong</h1>
<p class="abs hero-sub">Results of the first water and pollution recording<br>of Hong Kong Islands 80 km coastline.</p>
<svg class="abs circle-arrow" style="left:66px;top:436px" viewBox="0 0 62 62"><circle cx="31" cy="31" r="28" fill="none" stroke="#fff" stroke-width="3"/><path d="M35 20 L24 31 L35 42" fill="none" stroke="#fff" stroke-width="3"/></svg>
<svg class="abs circle-arrow" style="left:1070px;top:436px" viewBox="0 0 62 62"><circle cx="31" cy="31" r="28" fill="none" stroke="#fff" stroke-width="3"/><path d="M27 20 L38 31 L27 42" fill="none" stroke="#fff" stroke-width="3"/></svg>
<svg class="abs" style="left:572px;top:536px" width="62" height="62" viewBox="0 0 62 62"><circle cx="31" cy="31" r="30" fill="#1d7b82"/><path d="M25 20 L42 31 L25 42 Z" fill="none" stroke="#fff" stroke-width="2.5"/></svg>
<svg class="abs" style="left:585px;top:782px" width="34" height="44" viewBox="0 0 34 44"><path d="M7 8 L17 18 L27 8 M7 20 L17 30 L27 20" fill="none" stroke="#fff" stroke-width="3"/></svg>

<h2 class="abs welcome-title">Welcome to Our Team</h2>
<p class="abs welcome-text">If you would like more information from Tidewell Reclaim, please call their customer service line.</p>

<div class="abs water" role="img" aria-label="Photo of a shoreline covered in plastic waste"></div>
<h2 class="abs water-title">Water Pollution</h2>
<p class="abs water-text">Eighty percent of marine pollution comes from land. Air pollution is also a contributing factor by carrying off.</p>
<div class="abs btn-outline">LEARN MORE</div>

<h2 class="abs exp-heading">The<br>Expedition</h2>
<p class="abs exp-text">In May 2017 Mara Vennick and Joss Arlen completed the first successful coasteering expedition of Hong Kong Island.<br>In 6 days they climbed, swam, scrambled and hiked the entire coastline,took 51 water samples and mapped 163 trash pollution spots.<br>In May 2017 Mara Vennick and Joss Arlen completed the first successful coasteering expedition of Hong Kong Island.</p>
<div class="abs exp-photo" role="img" aria-label="Photo of washed-up debris on a rocky shore"></div>

<div class="abs partners"></div>
<svg class="abs" style="left:64px;top:2125px" width="1072" height="100" viewBox="0 0 1072 100" aria-hidden="true">
  <rect x="6" y="30" width="200" height="40" fill="#3a3a3a"/>
  <circle cx="348" cy="50" r="38" fill="#3c6fb4"/>
  <circle cx="671" cy="50" r="42" fill="#c4302b"/>
  <rect x="832" y="22" width="240" height="56" fill="#1f6b4a"/>
</svg>

<h2 class="abs section-title" style="top:2306px">Our Works</h2>
<div class="abs card" style="left:70px"><div class="card-img" role="img" aria-label="Photo of a green hillside above the sea" style="background:linear-gradient(180deg,#9cb6d6 0%,#5f8a4e 40%,#3f6a3a 75%,#3a7a9a 100%)"></div><div class="card-tag">NEWS</div><p class="card-text">Jacks Of All. Experts In All.</p></div>
<div class="abs card" style="left:452px"><div class="card-img" role="img" aria-label="Photo of volunteers collecting litter on a beach" style="background:linear-gradient(180deg,#6f7a80 0%,#5a5550 50%,#4a4440 100%)"></div><div class="card-tag">NEWS</div><p class="card-text">Jacks Of All. Experts In All.</p></div>
<div class="abs card" style="left:827px"><div class="card-img" role="img" aria-label="Photo of plastic bottles on a beach with birds overhead" style="background:linear-gradient(180deg,#c9d3da 0%,#a8b2b6 55%,#8a8f8c 100%)"></div><div class="card-tag">NEWS</div><p class="card-text">Jacks Of All. Experts In All.</p></div>

<div class="abs note"></div>
<h2 class="abs section-title" style="top:2836px">Send Us A Note</h2>
<div class="abs field" style="left:70px;top:2924px;width:501px;height:59px">*NAME</div>
<div class="abs field" style="left:70px;top:3024px;width:501px;height:59px">*EMAIL</div>
<div class="abs field" style="left:641px;top:2924px;width:491px;height:159px">*YOUR MESSAGE</div>
<div class="abs submit">SUBMIT</div>

<div class="abs footer"></div>
<div class="abs foot-col gold" style="left:70px"><span>Home</span><span>About</span><span>Work</span><span>Contact</span></div>
<div class="abs foot-col light" style="left:275px"><span>Chirper</span><span>Facepage</span><span>Snapgram</span><span>ViewStream</span></div>
<div class="abs foot-col light" style="left:510px"><span>Subscribe to Our<br>Newsletter</span><span>Privacy Policy</span><span>Terms &amp; Conditions</span></div>
<div class="abs foot-about-title">Shoreloop</div>
<p class="abs foot-about">We are a creative studio focusing on culture, luxury, editorial &amp; art. Somewhere between sophistication and simplicity.</p>
<div class="abs legal">@2017. All Rights Reserved.</div>

</body>
</html>
```